Criação de Kit com 6 Layouts de Post para Redes Sociais (Facebook, Instagram e etc) para Computador & Internet
A empresa queria:
" Software para gerenciamento de licitações, contratos, atas, empenhos, tudo relacionado a vendas ao governo. "

```html
<!DOCTYPE html>
<html lang="pt-BR">
<head>
<meta charset="UTF-8">
<title>Sistema Completo – Post</title>
<link href="https://fonts.googleapis.com/css2?family=Exo+2:wght@800&family=Open+Sans:wght@400;700&display=swap" rel="stylesheet">
<style>
  :root {
    --bg-deep: #0a2f8f;
    --bg-mid: #1556d6;
    --bg-light: #3f8ff0;
    --white: #ffffff;
    --navy: #071a4a;
    --rule: #0a1f5c;
    --frame: #6fb4ff;
    --photo-top: rgba(190, 200, 220, 0.55);
    --photo-mid: rgba(40, 60, 120, 0.55);
    --photo-low: rgba(10, 30, 90, 0.75);
    --icon-a: #1f58d8;
    --icon-b: #0b2a7a;
  }
  * { margin: 0; padding: 0; box-sizing: border-box; }
  html, body { width: 1200px; height: 1200px; overflow: hidden; }
  body { font-family: "Open Sans", sans-serif; }
  .post {
    position: relative;
    width: 1200px;
    height: 1200px;
    overflow: hidden;
    background: radial-gradient(circle at 70% 40%, var(--bg-light) 0%, var(--bg-mid) 40%, var(--bg-deep) 100%);
  }
  .check-icon {
    position: absolute;
    border-radius: 50%;
    background: radial-gradient(circle at 40% 35%, var(--icon-a), var(--icon-b));
    box-shadow: 0 20px 40px rgba(0, 0, 40, 0.35);
  }
  .check-icon--top { left: 560px; top: -20px; width: 210px; height: 210px; }
  .check-icon--bottom { left: -20px; top: 684px; width: 330px; height: 340px; }
  .presenter-photo {
    position: absolute;
    left: 610px;
    top: 40px;
    width: 590px;
    height: 1160px;
    border-radius: 280px 280px 0 0;
    background: linear-gradient(180deg, var(--photo-top) 0%, var(--photo-mid) 45%, var(--photo-low) 100%);
  }
  .headline {
    position: absolute;
    left: 60px;
    top: 138px;
    font-family: "Exo 2", sans-serif;
    font-weight: 800;
    font-size: 86px;
    line-height: 108px;
    color: var(--white);
    letter-spacing: 2px;
  }
  .divider {
    position: absolute;
    left: 0;
    top: 368px;
    width: 530px;
    height: 10px;
  }
  .body-copy {
    position: absolute;
    left: 62px;
    top: 404px;
    width: 540px;
    font-size: 30px;
    line-height: 44px;
    color: var(--white);
  }
  .brand-plate {
    position: absolute;
    left: 413px;
    top: 1042px;
    width: 375px;
    height: 180px;
    border-radius: 26px;
    background: var(--navy);
    border: 3px solid var(--frame);
    display: flex;
    align-items: center;
    justify-content: center;
    gap: 18px;
    padding-bottom: 24px;
  }
  .brand-dot {
    width: 46px;
    height: 46px;
    border-radius: 50%;
    background: var(--frame);
  }
  .brand-name {
    font-family: "Open Sans", sans-serif;
    font-weight: 700;
    font-size: 54px;
    color: var(--white);
    letter-spacing: 1px;
  }
</style>
</head>
<body>
  <main class="post">
    <div class="check-icon check-icon--top" role="img" aria-label="Ícone 3D de visto em círculo azul"></div>
    <div class="check-icon check-icon--bottom" role="img" aria-label="Ícone 3D de visto em círculo azul"></div>
    <div class="presenter-photo" role="img" aria-label="Foto de homem sorridente de terno fazendo sinal de positivo e segurando um notebook"></div>

    <h1 class="headline">SISTEMA<br>COMPLETO</h1>

    <svg class="divider" viewBox="0 0 530 10" aria-hidden="true">
      <rect x="0" y="3" width="520" height="4" fill="var(--rule)"/>
      <circle cx="522" cy="5" r="5" fill="var(--rule)"/>
    </svg>

    <p class="body-copy">Gerencie do acompanhamento<br>das licitações, passando pelas<br>atas e contratos, até o<br>recebimento do pedido,<br>entrega e cobrança.</p>

    <div class="brand-plate">
      <span class="brand-dot"></span>
      <span class="brand-name">LICITARE</span>
    </div>
  </main>
</body>
</html>
```